Book Cover Design Project

A non-fiction book on child protection, specifically... keeping young children safe from predators and keeping teenagers safe from themselves.

Title:
Beneath Our Roof

Subtitle:
A Guide To Keeping Your Children Safe

Author:
Martin Kellaway

```html
<!DOCTYPE html>
<html lang="en">
<head>
<meta charset="utf-8">
<title>Beneath Our Roof — Book Cover</title>
<link rel="stylesheet" href="https://fonts.googleapis.com/css2?family=Cinzel:wght@400;500;600&family=Marcellus&display=swap">
<style>
  :root {
    --ink: #000000;
    --title-cream: #d9ccb3;
    --subtitle-cream: #f1e9da;
    --author-cream: #e6dccb;
    --fabric-light: #e2d6c1;
    --fabric-mid: #c3ae8c;
    --fabric-dark: #8f7653;
    --press-light: #f3ede2;
    --press-shadow: rgba(96, 74, 45, 0.75);
  }
  html, body {
    margin: 0;
    padding: 0;
    width: 848px;
    height: 1200px;
    overflow: hidden;
    background: var(--ink);
  }
  .cover {
    position: relative;
    width: 848px;
    height: 1200px;
    background: var(--ink);
    overflow: hidden;
  }
  .title-band {
    position: absolute;
    top: 0;
    left: 0;
    width: 848px;
    height: 246px;
    background: var(--ink);
  }
  .book-title {
    position: absolute;
    top: 78px;
    left: 0;
    width: 848px;
    margin: 0;
    text-align: center;
    font-family: "Marcellus", "Optima", serif;
    font-weight: 400;
    font-size: 80px;
    line-height: 1;
    letter-spacing: 0;
    text-transform: uppercase;
    color: var(--title-cream);
    -webkit-text-stroke: 1.2px var(--title-cream);
  }
  .title-rule {
    position: absolute;
    top: 181px;
    left: 42px;
    width: 764px;
    height: 7px;
    background: var(--title-cream);
  }
  .fabric-art {
    position: absolute;
    top: 246px;
    left: 0;
    width: 848px;
    height: 838px;
    overflow: hidden;
    background:
      radial-gradient(ellipse 380px 420px at 300px 260px, rgba(232,224,210,0.9), rgba(232,224,210,0) 75%),
      radial-gradient(ellipse 500px 360px at 760px 820px, rgba(120,96,62,0.55), rgba(120,96,62,0) 75%),
      linear-gradient(155deg, var(--fabric-light) 0%, var(--fabric-mid) 55%, var(--fabric-dark) 100%);
  }
  .fabric-press {
    position: absolute;
    left: 250px;
    top: 215px;
    width: 330px;
    height: 340px;
    border-radius: 46% 40% 44% 50% / 42% 44% 52% 54%;
    background:
      radial-gradient(ellipse 60% 55% at 42% 45%, var(--press-light), rgba(236,228,214,0.85) 55%, rgba(214,200,176,0.6) 100%);
    box-shadow:
      22px 30px 38px 6px var(--press-shadow),
      -14px -16px 30px 4px rgba(250,246,238,0.55);
    filter: blur(9px);
  }
  .subtitle {
    position: absolute;
    top: 268px;
    left: 0;
    width: 848px;
    margin: 0;
    text-align: center;
    font-family: "Cinzel", "Trajan Pro", serif;
    font-weight: 500;
    font-size: 56px;
    line-height: 56px;
    letter-spacing: 3px;
    color: var(--subtitle-cream);
  }
  .author-band {
    position: absolute;
    left: 0;
    bottom: 0;
    width: 848px;
    height: 116px;
    background: var(--ink);
  }
  .author {
    position: absolute;
    left: 0;
    bottom: 30px;
    width: 848px;
    margin: 0;
    text-align: center;
    font-family: "Cinzel", "Trajan Pro", serif;
    font-weight: 600;
    font-size: 39px;
    letter-spacing: 2px;
    color: var(--author-cream);
  }
</style>
</head>
<body>
  <main class="cover">
    <header class="title-band">
      <h1 class="book-title">Beneath Our Roof</h1>
      <div class="title-rule"></div>
    </header>

    <div class="fabric-art" role="img" aria-label="Soft beige fabric with a small child's hand pressing through from behind">
      <div class="fabric-press"></div>
    </div>

    <h2 class="subtitle">A Guide To Keeping<br>Your Children Safe</h2>

    <footer class="author-band">
      <p class="author">BY: Martin Kellaway</p>
    </footer>
  </main>
</body>
</html>
```